Harbor Logistics Business card and letterhead
Professional business card
Professional
Calvin Marsh
Director of Operations
4538 E 61st Pl
Maple Grove, KS 66417-3814
cmarsh@harborlogisticsco.example
http://www.harborlogisticsco.example
Looking for something clean, professional, and simple. Fonts are optional, just flow with fonts in logo
On the back we would like the mission of "Carrying Every Promise" printed in some design. We would like the background to be a solid design from a logo color with white writing
This is our corporate logo

```html
<!DOCTYPE html>
<html lang="en">
<head>
<meta charset="utf-8">
<title>Harbor Logistics — Business Card</title>
<link href="https://fonts.googleapis.com/css2?family=Open+Sans:wght@400;600;700&display=swap" rel="stylesheet">
<style>
  :root {
    --stage: #e9e7e4;
    --card-white: #ffffff;
    --ink-navy: #1f2a44;
    --ink-grey: #6b6f78;
    --name-blue: #5457b4;
    --web-green: #2a9d48;
    --divider: #c9ccd2;
    --back-dark: #0a1020;
    --back-glow: #1d5fc4;
    --mark-blue: #2f86d8;
    --white: #ffffff;
  }
  * { box-sizing: border-box; margin: 0; padding: 0; }
  html, body { width: 1200px; height: 1030px; overflow: hidden; }
  body {
    background: var(--stage);
    font-family: "Open Sans", Arial, sans-serif;
    position: relative;
  }
  .card {
    position: absolute;
    left: 220px;
    width: 760px;
    height: 434px;
    border-radius: 4px;
    box-shadow: 0 6px 18px rgba(0,0,0,.18);
    overflow: hidden;
  }
  .card-front { top: 54px; background: var(--card-white); }
  .card-back {
    top: 542px;
    background: radial-gradient(circle at 50% 44%, var(--back-glow) 0%, #123a80 22%, var(--back-dark) 62%);
  }

  /* front */
  .brand {
    position: absolute;
    left: 52px;
    top: 160px;
    display: flex;
    align-items: center;
    gap: 14px;
  }
  .brand-dot {
    width: 64px; height: 64px; border-radius: 50%;
    background: var(--mark-blue);
  }
  .brand-name {
    font-weight: 700;
    font-size: 24px;
    letter-spacing: .5px;
    color: var(--ink-navy);
    text-transform: uppercase;
    line-height: 1.1;
  }
  .divider {
    position: absolute;
    left: 318px; top: 62px;
    width: 1px; height: 300px;
    background: var(--divider);
  }
  .contact {
    position: absolute;
    left: 346px; top: 66px;
    color: var(--ink-grey);
    font-size: 15px;
    line-height: 1.55;
  }
  .contact-name {
    font-size: 27px;
    font-weight: 600;
    color: var(--name-blue);
    line-height: 1.1;
  }
  .contact-title { font-size: 14px; margin-bottom: 30px; }
  .contact-web { color: var(--web-green); font-weight: 700; }

  /* back */
  .back-mark {
    position: absolute;
    left: 50%; top: 150px;
    width: 84px; height: 84px; margin-left: -42px;
    border-radius: 50%;
    background: var(--mark-blue);
  }
  .back-name {
    position: absolute; left: 0; right: 0; top: 248px;
    text-align: center;
    color: var(--white);
    font-weight: 700;
    font-size: 15px;
    letter-spacing: 2px;
    text-transform: uppercase;
  }
  .mission {
    position: absolute; left: 0; right: 0; top: 292px;
    text-align: center;
    color: var(--white);
    font-size: 15px;
    letter-spacing: 1px;
    text-transform: uppercase;
  }
</style>
</head>
<body>
  <section class="card card-front">
    <div class="brand">
      <span class="brand-dot"></span>
      <span class="brand-name">Harbor<br>Logistics</span>
    </div>
    <div class="divider"></div>
    <div class="contact">
      <p class="contact-name">Calvin Marsh</p>
      <p class="contact-title">Director of Operations</p>
      <p>4538 E 61st Pl</p>
      <p>Maple Grove, KS 66417-3814</p>
      <p>P: (555) 218-4470</p>
      <p>C: (555) 630-2915</p>
      <p>cmarsh@harborlogisticsco.example</p>
      <p class="contact-web">www.harborlogisticsco.example</p>
    </div>
  </section>

  <section class="card card-back">
    <span class="back-mark"></span>
    <p class="back-name">Harbor Logistics</p>
    <p class="mission">Carrying Every Promise</p>
  </section>
</body>
</html>
```